** Wanted ** Wordpress web design for scaffolding rental and construction company

We need a website design and must be functional to show a basic overview of what our company offers as a service. We have a domain name and a logo but we need web design. This web site should have another scaffolding rental page for construction and renovation as well as a quote section where customers can enter their personal information and also upload photos. The site% 26quot; www.corvithane.com% 26quot; should be intuitive, clear and classy ... The logo must be found on the site in several ways.

Target Market(s)

Professional and no professional

Coding

Coded - Design and coding required

Number of Pages Required

3 page

Font styles to use
Serif
Sans Serif
Decorative
Script

Requirements
Must have
• Our logo
Nice to have
• Slogan:% 26quot; The height% 26 # 224; port% 26 # 233; e hand% 26quot;

```html
<!DOCTYPE html>
<html lang="en">
<head>
<meta charset="utf-8">
<title>Corvithane – Scaffolding Rental</title>
<link href="https://fonts.googleapis.com/css2?family=Poppins:wght@300;400;500;600&display=swap" rel="stylesheet">
<style>
:root{
  --orange:#f0861f;
  --ink:#222;
  --text:#8a8a8a;
  --dark:#2a2a2a;
  --black:#111;
  --soft:#f6f6f6;
  --line:#e4e4e4;
  --white:#fff;
  --sky:#1f3f8c;
}
*{box-sizing:border-box;margin:0;padding:0}
html,body{width:1200px;height:2761px;overflow:hidden}
body{font-family:'Poppins',sans-serif;color:var(--ink);background:var(--white);position:relative;font-size:11px}
.abs{position:absolute}
ul{list-style:none}

.topbar{position:absolute;left:0;top:0;width:1200px;height:25px;background:var(--orange);color:#fff;font-size:9px}
.topbar .welcome{position:absolute;left:250px;top:7px}
.topbar .social{position:absolute;right:249px;top:6px;display:flex;gap:6px}
.topbar .social span{width:12px;height:12px;border:1px solid #fff;display:block}

.header{position:absolute;top:25px;left:0;width:1200px;height:104px}
.contact{position:absolute;top:24px;text-align:center}
.contact .ico{width:26px;height:26px;border:1px solid var(--orange);margin:0 auto 6px;display:flex;align-items:center;justify-content:center}
.contact .label{color:var(--orange);font-size:10px;line-height:12px}
.contact .value{font-size:11px;line-height:14px}
.contact.call{left:250px;text-align:left}
.contact.call .ico{margin-left:24px}
.contact.call .label{margin-left:20px}
.contact.mail{right:249px;text-align:right}
.contact.mail .ico{margin-right:32px;margin-left:auto}
.contact.mail .label{margin-right:40px}
.brand{position:absolute;left:547px;top:22px;width:107px;height:56px;display:flex;align-items:center;justify-content:center;gap:6px}
.brand .mark{width:12px;height:12px;background:var(--orange)}
.brand .name{font-size:13px;font-weight:600;color:var(--orange);letter-spacing:1px}

.nav{position:absolute;left:250px;top:129px;width:701px;height:42px;z-index:3}
.nav svg{position:absolute;left:0;top:0}
.nav ul{position:absolute;left:105px;top:0;display:flex;height:42px;align-items:center;font-size:10.5px;color:#fff}
.nav li{padding:0 16px;height:42px;line-height:42px}
.nav li.active{background:var(--orange);height:48px;margin-top:-6px;line-height:54px;padding:0 8px}
.nav li.quote{background:var(--orange);height:27px;line-height:27px;margin-left:20px;font-weight:500}

.hero{position:absolute;left:0;top:153px;width:1200px;height:403px;background:linear-gradient(135deg,#6f7a86 0%,#1f3a8a 45%,#173d9e 70%,#c2591c 100%)}
.hero-copy{position:absolute;left:250px;top:138px;color:#fff}
.hero-copy h1{font-weight:500;font-size:26px;line-height:30px;color:var(--orange)}
.hero-copy h1 .box{background:var(--orange);color:#fff;padding:0 8px}
.hero-copy h2{font-weight:300;font-size:24px;line-height:30px;color:#fff}
.hero-copy p{font-size:10.5px;line-height:15px;width:370px;margin-top:12px}
.quote-panel{position:absolute;left:731px;top:61px;width:220px;height:287px;background:rgba(20,30,70,.82);text-align:center;color:#fff}
.quote-panel h3{color:var(--orange);font-weight:500;font-size:18px;margin-top:26px}
.quote-panel .sub{font-size:10px}
.quote-panel .field{width:160px;height:26px;background:#fff;margin:10px auto 0;text-align:left;color:#777;font-size:8px;padding:8px 10px}
.quote-panel .upload{font-size:8.5px;margin-top:11px}
.quote-panel .slots{display:flex;gap:9px;justify-content:center;margin-top:6px}
.quote-panel .slots span{width:33px;height:33px;border:1px solid #fff;display:flex;align-items:center;justify-content:center}
.quote-panel .slots i{width:12px;height:12px;background:#999;color:#fff;font-style:normal;font-size:11px;line-height:12px}
.quote-panel .slots span:first-child i{background:var(--orange)}
.quote-panel .btn{width:160px;height:27px;background:var(--orange);margin:10px auto 0;font-size:10px;font-weight:500;line-height:27px}

.section-title{position:absolute;left:0;width:1200px;text-align:center}
.section-title h2{color:var(--orange);font-weight:500;font-size:18px}
.section-title .rule{display:flex;align-items:center;justify-content:center;gap:6px;margin-top:4px}
.section-title .rule i{width:50px;height:1px;background:#bbb}
.section-title .rule b{width:8px;height:8px;background:var(--orange);transform:rotate(45deg)}

.about{position:absolute;left:0;top:556px;width:1200px;height:335px}
.about .text{position:absolute;left:250px;top:119px;width:370px;color:var(--text);font-size:10.5px;line-height:15px}
.about ul{margin-top:9px}
.about li{line-height:18px;padding-left:14px;position:relative}
.about li:before{content:"";position:absolute;left:1px;top:6px;width:6px;height:6px;background:var(--orange);transform:rotate(45deg)}
.about .last{color:var(--ink)}
.photo{background:linear-gradient(160deg,#4f8fd0,#8a6a4a 55%,#3a3a3a)}
.about .frame{position:absolute;left:678px;top:123px;width:273px;height:150px;border-left:2px solid var(--orange);border-bottom:2px solid var(--orange)}
.about .photo{position:absolute;left:681px;top:122px;width:270px;height:148px}

.features{position:absolute;left:0;top:891px;width:1200px;height:448px;background:var(--soft)}
.features .frame{position:absolute;left:320px;top:58px;width:262px;height:270px;border-top:2px solid var(--orange);border-right:2px solid var(--orange)}
.features .photo{position:absolute;left:250px;top:60px;width:330px;height:326px;background:linear-gradient(90deg,#c8532a 0%,#b74a26 40%,#a8a8a8 45%,#8b8b8b 100%)}
.card{position:absolute;width:161px;height:157px;background:#fff;border:1px solid #ececec;text-align:center}
.card .icon{width:30px;height:26px;margin:18px auto 0;border:2px solid #333;border-bottom:3px solid var(--orange)}
.card h4{color:var(--orange);font-weight:400;font-size:10px;margin-top:16px}
.card .bar{width:36px;height:1px;background:#999;margin:9px auto}
.card p{color:var(--text);font-size:9px;line-height:15px;padding:0 16px}
.card.lead h3{color:var(--orange);font-weight:500;font-size:18px;line-height:21px;margin-top:16px}
.card.lead .bar{margin:15px auto 18px}
.card.lead .btn{display:inline-block;background:var(--orange);color:#fff;font-size:10px;font-weight:500;padding:6px 17px}

.projects{position:absolute;left:0;top:1339px;width:1200px;height:616px}
.projects .intro{position:absolute;left:0;width:1200px;top:104px;text-align:center;color:var(--text);font-size:9.5px;line-height:15px}
.filters{position:absolute;left:441px;top:157px;display:flex;border:1px solid var(--orange);height:27px;font-size:9.5px}
.filters span{padding:0 17px;line-height:25px;border-left:1px solid #ddd}
.filters span:first-child{background:var(--orange);color:#fff;border:0;padding:0 18px}
.tile{position:absolute;width:161px;height:161px}
.t1{background:linear-gradient(160deg,#2b3f7a,#c87a3c 60%,#6e5a4a)}
.t2{background:linear-gradient(150deg,#8fb4dc,#6d4b2e 50%,#3a2a1e)}
.t3{background:linear-gradient(180deg,#3d86d4,#4a7fc0 55%,#6a5040)}
.t4{background:linear-gradient(180deg,#2d7fd8,#7aa6d4 60%,#e0b020)}
.tile .overlay{position:absolute;left:8px;top:8px;width:145px;height:145px;background:#fff;text-align:center}
.tile .overlay h5{color:var(--orange);font-weight:400;font-size:10px;margin-top:8px}
.tile .overlay p{color:var(--text);font-size:8.5px;line-height:10.5px;padding:4px 16px 0}

.testimonials{position:absolute;left:0;top:1955px;width:1200px;height:415px;background:#f8f8f8}
.quote-box{position:absolute;top:123px;width:326px;height:108px;background:#fff;border:1px solid #ececec;color:var(--text);font-size:9px;line-height:18px;padding:15px 40px 0 46px}
.quote-box:after{content:"";position:absolute;left:70px;bottom:-8px;width:14px;height:14px;background:#fff;transform:rotate(45deg);border-right:1px solid #ececec;border-bottom:1px solid #ececec}
.person{position:absolute;top:257px;display:flex;align-items:center;gap:12px}
.person .avatar{width:46px;height:46px;border-radius:50%;background:linear-gradient(135deg,#dcdcdc,#2f3440)}
.person h6{color:var(--orange);font-weight:500;font-size:11px}
.person p{color:#bbb;font-size:9px;margin-top:6px}
.arrows{position:absolute;top:334px;left:576px;display:flex;gap:10px}
.arrows span{width:20px;height:20px;border:1px solid #ccc;display:flex;align-items:center;justify-content:center}
.arrows span+span{border-color:var(--orange)}

.partners{position:absolute;left:0;top:2370px;width:1200px;height:108px;display:flex;justify-content:space-between;align-items:center;padding:0 249px 0 250px;color:#555;font-size:12px;font-weight:500}
.partners .p{display:flex;align-items:center;gap:6px}
.partners .p i{width:22px;height:22px;border-radius:50%;background:#666}

.footer{position:absolute;left:0;top:2478px;width:1200px;height:247px;background:var(--dark);color:#fff}
.footer .logo{position:absolute;left:250px;top:30px;width:195px;height:85px;display:flex;align-items:center;gap:12px}
.footer .logo .mark{width:26px;height:26px;background:var(--orange)}
.footer .logo .name{font-size:22px;font-weight:600;color:var(--orange);letter-spacing:1px}
.footer .about-text{position:absolute;left:250px;top:135px;width:200px;font-size:11px;line-height:20px}
.footer h4{position:absolute;font-weight:500;font-size:11px;top:77px}
.links{position:absolute;left:517px;top:101px;width:167px}
.links li{font-size:11px;border-bottom:1px solid #aaa;height:27px;line-height:27px;padding-left:26px;position:relative}
.links li:before{content:"";position:absolute;left:10px;top:11px;width:5px;height:5px;background:#fff}
.location{position:absolute;left:753px;top:103px;font-size:11px;line-height:14px;width:200px}
.location div{margin-bottom:14px}
.bottombar{position:absolute;left:0;top:2725px;width:1200px;height:36px;background:var(--orange);color:#fff;font-size:7px}
.bottombar span{position:absolute;left:250px;top:14px}
</style>
</head>
<body>

<div class="topbar">
  <span class="welcome">Wellcome To Corvithane - Rent Every Thing</span>
  <div class="social"><span></span><span></span><span></span></div>
</div>

<header class="header">
  <div class="contact call">
    <div class="ico"><svg width="12" height="12" viewBox="0 0 24 24"><path d="M6.6 10.8a15 15 0 0 0 6.6 6.6l2.2-2.2a1 1 0 0 1 1-.25 11.4 11.4 0 0 0 3.6.6 1 1 0 0 1 1 1V20a1 1 0 0 1-1 1A17 17 0 0 1 3 4a1 1 0 0 1 1-1h3.5a1 1 0 0 1 1 1c0 1.25.2 2.45.6 3.6a1 1 0 0 1-.25 1z" fill="#f0861f"/></svg></div>
    <div class="label">CALL US</div>
    <div class="value">+12 555 014 7730</div>
  </div>
  <div class="brand"><span class="mark"></span><span class="name">CORVITHANE</span></div>
  <div class="contact mail">
    <div class="ico"><svg width="12" height="12" viewBox="0 0 24 24"><path d="M6.6 10.8a15 15 0 0 0 6.6 6.6l2.2-2.2a1 1 0 0 1 1-.25 11.4 11.4 0 0 0 3.6.6 1 1 0 0 1 1 1V20a1 1 0 0 1-1 1A17 17 0 0 1 3 4a1 1 0 0 1 1-1h3.5a1 1 0 0 1 1 1c0 1.25.2 2.45.6 3.6a1 1 0 0 1-.25 1z" fill="#f0861f"/></svg></div>
    <div class="label">EMAIL US</div>
    <div class="value">email@corvithane.com</div>
  </div>
</header>

<nav class="nav">
  <svg width="701" height="42"><polygon points="0,0 701,0 658,42 43,42" fill="#111"/></svg>
  <ul>
    <li class="active">HOME</li><li>RENTAL</li><li>SERVICES</li><li>BLOG</li><li>CONTACT US</li><li class="quote">GET A QUOTE</li>
  </ul>
</nav>

<section class="hero" role="img" aria-label="Photo of steel scaffolding tubes and couplers against a deep blue sky">
  <div class="hero-copy">
    <h1>SCAFFOLDING <span class="box">RENTAL FOR</span></h1>
    <h2>CONSTRUCTION &amp; RENOVATION</h2>
    <p>Lorem ipsum dolor sit amet, consectetur adipiscing elit, sed do eiusmod tempor incididunt ut labore et dolore magna aliqua. Quis ipsum suspendisse ultrices gravida. Risus commodo viverra maecenas accumsan lacus vel facilisis.</p>
  </div>
  <form class="quote-panel">
    <h3>GET A QUOTE</h3>
    <div class="sub">Lorem ipsum dolor sit amet.</div>
    <div class="field">Full Name</div>
    <div class="field">Email</div>
    <div class="field">Phone</div>
    <div class="upload">Upload Your Site Images:</div>
    <div class="slots"><span><i>+</i></span><span><i>+</i></span><span><i>+</i></span><span><i>+</i></span></div>
    <div class="btn">GET A QUOTE</div>
  </form>
</section>

<section class="about">
  <div class="section-title" style="top:56px"><h2>ABOUT US</h2><div class="rule"><i></i><b></b><i></i></div></div>
  <div class="text">
    <p>Lorem ipsum dolor sit amet, consectetur adipiscing elit, sed do eiusmod tempor incididunt ut labore et dolore magna aliqua. Quis ipsum suspendisse ultrices gravida. Risus commodo viverra maecenas accumsan lacus vel facilisis.</p>
    <ul>
      <li>Advanced product range</li>
      <li>Substantial stockholding</li>
      <li>Unrivalled "know how"</li>
      <li>"On time" supply</li>
    </ul>
    <p class="last">Total commitment to customer support</p>
  </div>
  <div class="frame"></div>
  <div class="photo" role="img" aria-label="Photo of a building under construction wrapped in scaffolding"></div>
</section>

<section class="features">
  <div class="frame"></div>
  <div class="photo" role="img" aria-label="Photo of red and silver scaffolding towers on a building facade"></div>
  <div class="card lead" style="left:612px;top:59px">
    <h3>HIGH<br>QUALITY<br>SERVICE</h3>
    <div class="bar"></div>
    <span class="btn">GET A QUOTE</span>
  </div>
  <div class="card" style="left:790px;top:59px">
    <div class="icon" role="img" aria-label="Scaffold frame icon"></div>
    <h4>ROOFING SCAFFOLDS</h4><div class="bar"></div>
    <p>Lorem ipsum dolor sit amet, consectetur adipiscing elit, sed do eiusmod tempor</p>
  </div>
  <div class="card" style="left:612px;top:233px">
    <div class="icon" role="img" aria-label="Scaffold frame icon"></div>
    <h4>COMMERCIAL SCAFFOLDS</h4><div class="bar"></div>
    <p>Lorem ipsum dolor sit amet, consectetur adipiscing elit, sed do eiusmod tempor</p>
  </div>
  <div class="card" style="left:790px;top:233px">
    <div class="icon" role="img" aria-label="Scaffold frame icon"></div>
    <h4>DOMESTIC SCAFFOLDS</h4><div class="bar"></div>
    <p>Lorem ipsum dolor sit amet, consectetur adipiscing elit, sed do eiusmod tempor</p>
  </div>
</section>

<section class="projects">
  <div class="section-title" style="top:56px"><h2>OUR PROJECTS</h2><div class="rule"><i></i><b></b><i></i></div></div>
  <p class="intro">Lorem ipsum dolor sit amet, consectetur adipiscing elit, sed do eiusmod<br>tempor incididunt ut labore et dolore magna aliqua.</p>
  <div class="filters"><span>ALL</span><span>COMMERCIAL</span><span>DOMESTIC</span><span>ROOFING</span></div>

  <div class="tile t1" style="left:250px;top:215px" role="img" aria-label="Project photo: scaffold walkway at sunset"></div>
  <div class="tile t2" style="left:430px;top:215px" role="img" aria-label="Project photo: scaffolded building">
    <div class="overlay">
      <svg width="30" height="30" viewBox="0 0 30 30" style="margin-top:24px"><circle cx="17" cy="12" r="8" fill="none" stroke="#222" stroke-width="2"/><line x1="11" y1="18" x2="4" y2="25" stroke="#222" stroke-width="3"/><line x1="13" y1="12" x2="21" y2="12" stroke="#222" stroke-width="2"/><line x1="17" y1="8" x2="17" y2="16" stroke="#222" stroke-width="2"/></svg>
      <h5>LOREM LTD.</h5>
      <p>Lorem ipsum dolor sit amet, consectetur adipi-scing elit, sed do eiusmod tempor incididunt.</p>
    </div>
  </div>
  <div class="tile t3" style="left:609px;top:215px" role="img" aria-label="Project photo: scaffolding on a facade under blue sky"></div>
  <div class="tile t4" style="left:789px;top:215px" role="img" aria-label="Project photo: scaffold poles with yellow boards"></div>
  <div class="tile t1" style="left:250px;top:395px" role="img" aria-label="Project photo: scaffold walkway at sunset"></div>
  <div class="tile t2" style="left:430px;top:395px" role="img" aria-label="Project photo: scaffolded building"></div>
  <div class="tile t3" style="left:609px;top:395px" role="img" aria-label="Project photo: scaffolding on a facade under blue sky"></div>
  <div class="tile t4" style="left:789px;top:395px" role="img" aria-label="Project photo: scaffold poles with yellow boards"></div>
</section>

<section class="testimonials">
  <div class="section-title" style="top:58px"><h2>TESTIMONIAL</h2><div class="rule"><i></i><b></b><i></i></div></div>
  <div class="quote-box" style="left:260px">Lorem ipsum dolor sit amet, consectetur adipiscing elit, sed do eiusmod tempor incididunt ut labore et dolore magna aliqua. Quis ipsum suspendisse ultrices gravida. Risus commodo viverra maecenas accumsan lacus vel facilisis.</div>
  <div class="quote-box" style="left:614px">Lorem ipsum dolor sit amet, consectetur adipiscing elit, sed do eiusmod tempor incididunt ut labore et dolore magna aliqua. Quis ipsum suspendisse ultrices gravida. Risus commodo viverra maecenas accumsan lacus vel facilisis.</div>
  <div class="person" style="left:309px"><div class="avatar" role="img" aria-label="Client portrait"></div><div><h6>Elias Varn</h6><p>CEO, Lorem Ipsum</p></div></div>
  <div class="person" style="left:663px"><div class="avatar" role="img" aria-label="Client portrait"></div><div><h6>Elias Varn</h6><p>CEO, Lorem Ipsum</p></div></div>
  <div class="arrows">
    <span><svg width="8" height="8" viewBox="0 0 8 8"><polyline points="5,1 2,4 5,7" fill="none" stroke="#555" stroke-width="1.2"/></svg></span>
    <span><svg width="8" height="8" viewBox="0 0 8 8"><polyline points="3,1 6,4 3,7" fill="none" stroke="#f0861f" stroke-width="1.2"/></svg></span>
  </div>
</section>

<section class="partners">
  <div class="p"><i></i>Veldmark</div>
  <div class="p"><i></i>Orlisse</div>
  <div class="p"><i></i>Brightwane</div>
  <div class="p"><i></i>Tessaly Arts</div>
  <div class="p"><i></i>Quarnel Care</div>
</section>

<footer class="footer">
  <div class="logo"><span class="mark"></span><span class="name">CORVITHANE</span></div>
  <p class="about-text">Lorem ipsum dolor sit amet, consecte-tur adipiscing elit, sed do eiusmod tempor incididunt ut labore et dolore magna aliqua.</p>
  <h4 style="left:517px">IMPORTANT LINKS</h4>
  <ul class="links"><li>Home</li><li>About</li><li>Services</li><li>Blog</li><li>Contact</li></ul>
  <h4 style="left:753px">OUR LOCATION</h4>
  <div class="location">
    <div>Address:<br>Harlow Yard, 48 Brenmoor Lane, Leeds, LS9 2QT, United Kingdom.</div>
    <div>Phone:<br>(01) 555 028 4416</div>
    <div>Email:<br>Email@corvithane.com</div>
  </div>
</footer>

<div class="bottombar"><span>© Copyright 2020. All Right Reserved.</span></div>

</body>
</html>
```